Marigold Hollow WordPress Website

Wordpress/Divi website for our daycare/learning center. Please see directions and layout documents.
Target Market(s)
Primary Market is for existing clientele. Parents of young children age 1-7 yrs old. Parents are well educated, between 23-40 years of age.
Industry/Entity Type
Early Learning Center
Coding
Coded - Design and coding required
Font styles to use
Sans Serif
Requirements
Must have
- • The website MUST be responsive and optimized for mobile devices like iPads and cellphones.
• Use logo from file.
• Pictures of people, they should be of children/staff in our target markets.
• Utuilize linking to Tallyroost for Scheduling and News
• Social media links in all pages.
• Include Chamber of Commerce logo in all pages.
• Use placeholder pics wherever you feel a pic should be
Nice to have
- LOOK AND FEEL
Please do NOT copy, but https://www.quillbrookacademy.com is an example of overall look and feel. User (Parent) friendly, Clean, easy to navigate, visually appealing without being cluttered. Colors should be pleasing to the eye (No grays)
Should not have
- NO custom coding. Site must be 100% constructed using WordPress/Elegant Themes/Divi. Site will be stored at HostaLoom Supported Wordpress.

```html
<!DOCTYPE html>
<html lang="en">
<head>
<meta charset="utf-8">
<title>Marigold Hollow – Childhood Learning Center</title>
<link href="https://fonts.googleapis.com/css2?family=IBM+Plex+Sans:wght@400;500;600;700&family=Montserrat:wght@500;800;900&display=swap" rel="stylesheet">
<style>
:root{
  --red:#c8102e;
  --ink:#1d1d1f;
  --text:#2b2b2b;
  --paper:#f4f2f3;
  --white:#ffffff;
  --line:#d9d6d8;
  --brand-purple:#5a4fd1;
}
*{box-sizing:border-box;margin:0;padding:0}
html,body{width:694px;height:1200px;overflow:hidden}
body{position:relative;background:var(--white);font-family:"IBM Plex Sans",sans-serif;color:var(--text)}
.abs{position:absolute}

/* header */
.site-header{left:0;top:0;width:694px;height:60px;background:var(--paper)}
.logo-badge{left:68px;top:4px;width:90px;height:62px;background:var(--white);border-radius:0 0 45px 45px;display:flex;flex-direction:column;align-items:center;justify-content:center;gap:3px}
.logo-badge .dot{width:12px;height:12px;border-radius:50%;background:var(--red)}
.logo-name{font-weight:700;font-size:11px;color:var(--red);line-height:1}
.call{left:452px;top:12px;display:flex;align-items:center;gap:5px}
.call .lab{font-size:5px;color:var(--ink);line-height:1}
.call .num{font-size:10.5px;color:var(--ink);font-weight:500;line-height:1.1}
.search{left:555px;top:12px;width:63px;height:18px;border:1px solid #999;background:var(--white);font-size:5.5px;display:flex;align-items:center;justify-content:space-between;padding:0 5px;color:#333}
.main-nav{left:180px;top:40px;display:flex;gap:17px;font-size:7.4px;font-weight:500;color:var(--ink);letter-spacing:.1px}
.main-nav .current{color:var(--red);text-decoration:underline}

/* hero */
.hero{left:0;top:60px;width:694px;height:320px;background:linear-gradient(100deg,#e8d9c4 0%,#f2c97a 22%,#f0b69a 38%,#ede8e4 58%,#f6f4f4 72%,#ffffff 100%)}
.hero-title{left:436px;top:122px;font-family:"Montserrat",sans-serif;font-size:26.5px;line-height:30.5px;color:var(--ink)}
.hero-title b{font-weight:900;display:block}
.hero-title span{font-weight:500;display:block}
.btn{left:440px;top:225px;width:69px;height:22px;background:var(--red);color:var(--white);font-family:"Montserrat",sans-serif;font-weight:800;font-size:7px;display:flex;align-items:center;justify-content:center}
.arrow{top:210px;width:20px;height:20px;background:#2a2a2a;display:flex;align-items:center;justify-content:center}
.dots{left:328px;top:353px;display:flex;gap:8px}
.dots i{width:5.5px;height:5.5px;border-radius:50%;background:#222;display:block}
.dots i.on{background:var(--red);box-shadow:0 0 0 1.2px #fff}

/* philosophy */
.section-title{font-weight:700;font-size:14.5px;color:var(--ink);letter-spacing:.2px}
.rule{height:2px;width:30px;background:var(--red)}
.body-copy{font-size:7.4px;line-height:11.1px;text-align:justify;width:273px;color:var(--text)}
.photo{background:linear-gradient(135deg,#8a6a4a,#c43a2a 40%,#c9b9c6 70%,#6fa3d9)}

/* contact */
.contact{left:0;top:699px;width:694px;height:330px;background:linear-gradient(180deg,#f4eeee 0%,#f3efef 55%,#efe4d8 80%,#f0f2f4 100%)}
.card{width:236px;height:226px;background:var(--white);border:1px solid #cfcfcf}
.card .pic{height:145px}
.info{position:absolute;left:12px;display:flex;gap:8px;align-items:flex-start;font-size:7.3px;line-height:11px;color:var(--ink)}
.icon{width:17px;height:17px;border-radius:50%;background:var(--red);flex:none;display:flex;align-items:center;justify-content:center}
.info strong{font-weight:600;font-size:6.8px}

/* footer */
.site-footer{left:0;top:1028px;width:694px;height:172px;background:var(--paper)}
.foot-head{font-size:7px;font-weight:600;color:var(--red);padding-bottom:4px;border-bottom:1px solid var(--red)}
.foot-links{font-size:7.3px;line-height:13px;color:var(--ink);list-style:none}
.social{display:flex;gap:4px}
.social span{width:16px;height:16px;border-radius:50%;display:block}
.copyright{font-size:6.8px;color:var(--ink)}
</style>
</head>
<body>

<header class="site-header abs">
  <div class="logo-badge abs"><span class="dot"></span><span class="logo-name">Marigold Hollow</span></div>
  <div class="call abs">
    <svg width="14" height="14" viewBox="0 0 24 24" fill="none" stroke="#222" stroke-width="2"><path d="M5 3h4l2 5-3 2a11 11 0 0 0 6 6l2-3 5 2v4a2 2 0 0 1-2 2A17 17 0 0 1 3 5a2 2 0 0 1 2-2z"/></svg>
    <div><div class="lab">CALL US</div><div class="num">555.010.4821</div></div>
  </div>
  <div class="search abs">SEARCH
    <svg width="6" height="6" viewBox="0 0 10 10" fill="none" stroke="#555" stroke-width="1.4"><circle cx="4" cy="4" r="3"/><path d="M6.3 6.3 9 9"/></svg>
  </div>
  <nav class="main-nav abs">
    <span class="current">OUR TEAM</span><span>FLEX SCHEDULING</span><span>SITTER SERVICE</span><span>AWARDS/ACCOLADES</span><span>JOIN OUR TEAM</span><span>OUR PHILOSOPHY</span>
  </nav>
</header>

<section class="hero abs" role="img" aria-label="Laughing child playing with colourful foam building blocks at a table"></section>
<h1 class="hero-title abs"><b>CHILDHOOD</b><span>LEARNING</span><b>CENTER</b></h1>
<a class="btn abs">READ MORE</a>
<div class="arrow abs" style="left:0"><svg width="8" height="10" viewBox="0 0 8 10" fill="none" stroke="#fff" stroke-width="1.5"><path d="M6 1 2 5l4 4"/></svg></div>
<div class="arrow abs" style="left:674px"><svg width="8" height="10" viewBox="0 0 8 10" fill="none" stroke="#fff" stroke-width="1.5"><path d="M2 1l4 4-4 4"/></svg></div>
<div class="dots abs"><i></i><i></i><i class="on"></i><i></i><i></i></div>

<section>
  <h2 class="section-title abs" style="left:75px;top:415px">OUR PHILOSOPHY</h2>
  <div class="rule abs" style="left:76px;top:437px"></div>
  <p class="body-copy abs" style="left:76px;top:462px">It is our goal at Marigold Hollow to make each child feel safe and secure, while exposing them to appropriate developmental skills and building a positive self-concept. We encourage children to take risks and learn from their mistakes in both academic and social settings. We use a positive behavior approach which consists of specific praise, modeling appropriate behaviors, and providing children with acceptable choices. We teach children to develop behavior habits and attitudes that will allow them to interact well with others in school and throughout life.</p>
  <p class="body-copy abs" style="left:76px;top:568px">At Marigold Hollow, we strive to prepare our children for the next step they will be taking-whether it be moving from the infant room to the toddler room, or leaving our pre-kindergarten program to enter kindergarten in another school. Children experience growth and learning in their social- emotional, physical, language, and cognitive development. We provide children with the tools they need to be successful and encourage them to use these tools in a way that works best for them. Thoughout every child’s experience at Marigold Hollow, families will feel supported and nurtured in their child rearing efforts.</p>
  <div class="photo abs" style="left:381px;top:416px;width:237px;height:246px" role="img" aria-label="Toddler in a red sweater painting at a craft table"></div>
</section>

<section class="contact abs" role="img" aria-label="Soft blurred background of a child with toy blocks">
  <h2 class="section-title abs" style="left:0;width:694px;text-align:center;top:24px">CONTACT US</h2>
  <div class="rule abs" style="left:333px;top:48px"></div>

  <div class="card abs" style="left:101px;top:73px">
    <div class="pic" style="background:linear-gradient(180deg,#cbb994 0%,#d9cdb1 45%,#7d7f86 75%,#8a8a8a 100%)" role="img" aria-label="Children and staff holding a banner in front of the Alderbrook center"></div>
    <div class="info" style="top:155px"><span class="icon"><svg width="9" height="9" viewBox="0 0 10 10" fill="none" stroke="#fff" stroke-width="1.2"><circle cx="5" cy="5" r="3.8"/><path d="M5 3v2h-1.5"/></svg></span><div>Hours: 6:30 AM – 6:00 PM<br>Serving children 8 weeks to 12 years.</div></div>
    <div class="info" style="top:187px"><span class="icon"><svg width="8" height="10" viewBox="0 0 8 10" fill="#fff"><path d="M4 0a3.5 3.5 0 0 0-3.5 3.5C.5 6 4 10 4 10s3.5-4 3.5-6.5A3.5 3.5 0 0 0 4 0zm0 5a1.4 1.4 0 1 1 0-2.8A1.4 1.4 0 0 1 4 5z"/></svg></span><div><strong>DIRECTIONS:</strong><br>4120 Route 12, Alderbrook, NY</div></div>
  </div>

  <div class="card abs" style="left:359px;top:73px">
    <div class="pic" style="background:linear-gradient(180deg,#6f86d8 0%,#b9c6ea 40%,#dfe4ee 60%,#5d5a4c 80%,#3f4a2f 100%)" role="img" aria-label="Exterior of the Lindenport center under a blue sky"></div>
    <div class="info" style="top:155px"><span class="icon"><svg width="9" height="9" viewBox="0 0 10 10" fill="none" stroke="#fff" stroke-width="1.2"><circle cx="5" cy="5" r="3.8"/><path d="M5 3v2h-1.5"/></svg></span><div>Hours: 6:30 AM – 6:00 PM<br>Serving children 8 weeks to 12 years.</div></div>
    <div class="info" style="top:187px"><span class="icon"><svg width="8" height="10" viewBox="0 0 8 10" fill="#fff"><path d="M4 0a3.5 3.5 0 0 0-3.5 3.5C.5 6 4 10 4 10s3.5-4 3.5-6.5A3.5 3.5 0 0 0 4 0zm0 5a1.4 1.4 0 1 1 0-2.8A1.4 1.4 0 0 1 4 5z"/></svg></span><div><strong>DIRECTIONS:</strong><br>88 Fernway Highway, Lindenport, NY 12000</div></div>
  </div>
</section>

<footer class="site-footer abs">
  <div class="abs" style="left:76px;top:40px;display:flex;align-items:center;gap:4px">
    <span style="width:10px;height:10px;border-radius:50%;background:var(--red);display:block"></span>
    <span class="logo-name">Marigold Hollow</span>
  </div>
  <div class="abs" style="left:231px;top:30px;width:158px">
    <div class="foot-head">MENU</div>
    <ul class="foot-links abs" style="left:0;top:23px"><li>Our Team</li><li>Flex Scheduling</li><li>Sitter Service</li></ul>
    <ul class="foot-links abs" style="left:95px;top:23px;white-space:nowrap"><li>Awards/Accolades</li><li>Join our team</li><li>Our Philosophy</li></ul>
  </div>
  <div class="abs" style="left:444px;top:30px;width:158px">
    <div class="foot-head">FOLLOW US</div>
    <div class="social abs" style="left:0;top:23px"><span style="background:#3b5bab"></span><span style="background:#2aa3e6"></span><span style="background:#1b2a6b"></span></div>
  </div>
  <div class="abs" style="left:75px;top:114px;width:544px;height:1px;background:var(--line)"></div>
  <p class="copyright abs" style="left:75px;top:137px">Copyright © 2020 All Rights Reserved</p>
  <div class="abs" style="left:421px;top:134px;width:76px;height:20px;border-radius:3px;background:#d8d2c4" role="img" aria-label="Ashvale County Chamber of Commerce member badge"></div>
  <div class="abs" style="left:522px;top:133px;font-size:14px;font-weight:500;color:var(--brand-purple)">Tallyroost</div>
</footer>

</body>
</html>
```